Not-for-profit Community Law Business Card

Not-for-Profit community law firm are looking for new business card design to accompany a new logo.
The cards are to assist the organisation in reaching their strategic objective of generating greater networking amongst the community; specifically with other service providers, clients, and community influencers.
It should stand out. Be professional, strong, creative, clear in detail. The logo should be a major feature of the design.
Updates

Hi All,

Thank you for the submissions so far. I have uploaded the logo and colour details again, as requested. If you have any further issues downloading them or need a different format please contact me on jess_harlow@bvm.net.au

Kind regards,

Industry/Entity Type

Law Firm

Requirements
Must have
• Logo (attached)
Person's name
Position
Phone
Fax
Email
PO Box address
Website
Colours from the logo.

```html
<!DOCTYPE html>
<html lang="en">
<head>
<meta charset="utf-8">
<title>Harbour Point Legal Centre – Business Card</title>
<link rel="stylesheet" href="https://fonts.googleapis.com/css2?family=Montserrat:wght@400;500;600&display=swap">
<style>
  :root {
    --backdrop: #e4e2de;
    --card: #f7f7f6;
    --brand-blue: #1c63b3;
    --brand-navy: #1e2a72;
    --ink: #262626;
    --ink-soft: #3a3a3a;
  }
  * { box-sizing: border-box; margin: 0; padding: 0; }
  html, body {
    width: 1200px;
    height: 900px;
    overflow: hidden;
    background: var(--backdrop);
    font-family: "Montserrat", Arial, sans-serif;
  }
  .stage {
    width: 1200px;
    height: 900px;
    display: flex;
    align-items: center;
    justify-content: center;
  }
  .business-card {
    position: relative;
    width: 980px;
    height: 560px;
    background: var(--card);
    box-shadow: 0 6px 22px rgba(0,0,0,0.12);
  }
  .brand {
    position: absolute;
    left: 70px;
    top: 110px;
    display: flex;
    align-items: center;
    gap: 22px;
  }
  .brand-mark {
    width: 74px;
    height: 74px;
    border-radius: 50%;
    background: var(--brand-blue);
  }
  .brand-name {
    color: var(--brand-blue);
    font-weight: 600;
    font-size: 40px;
    line-height: 1.1;
    letter-spacing: 0.02em;
  }
  .brand-name .line-two {
    display: block;
    font-size: 24px;
    letter-spacing: 0.12em;
  }
  .website {
    position: absolute;
    right: 60px;
    top: 250px;
    color: var(--brand-navy);
    font-weight: 600;
    font-size: 24px;
    letter-spacing: 0.01em;
  }
  .person {
    position: absolute;
    left: 70px;
    top: 318px;
    display: flex;
    align-items: baseline;
    gap: 16px;
    color: var(--ink);
  }
  .person-name {
    font-weight: 400;
    font-size: 36px;
    letter-spacing: 0.06em;
  }
  .divider {
    font-size: 34px;
    font-weight: 500;
  }
  .person-role {
    font-size: 22px;
    letter-spacing: 0.08em;
  }
  .contact {
    position: absolute;
    left: 70px;
    top: 392px;
    color: var(--ink-soft);
    font-size: 22px;
    line-height: 1.4;
    letter-spacing: 0.02em;
  }
  .contact .label {
    color: var(--brand-navy);
    font-weight: 600;
    margin-right: 8px;
  }
  .contact .gap { margin-left: 16px; }
  .address {
    margin-top: 14px;
    font-size: 24px;
    line-height: 1.3;
  }
</style>
</head>
<body>
<main class="stage">
  <article class="business-card">
    <header class="brand">
      <span class="brand-mark" aria-hidden="true"></span>
      <span class="brand-name">Harbour Point<span class="line-two">Legal Centre Inc.</span></span>
    </header>

    <p class="website">harbourpointlegal.org</p>

    <div class="person">
      <h1 class="person-name">DANA WHITFIELD</h1>
      <span class="divider">|</span>
      <span class="person-role">MANAGER</span>
    </div>

    <address class="contact">
      <div><span class="label">t</span>555.014.2281<span class="gap"><span class="label">f</span>555.014.2290</span></div>
      <div><span class="label">e</span>dwhitfield@harbourpointlegal.org</div>
      <div class="address">42 Cedar Lane, Ste. 210<br>Fairview, TX 75000</div>
    </address>
  </article>
</main>
</body>
</html>
```